Unternehmen für Wimpernverlängerung & -lifting benötigt Flyer-Design
Zielgruppe
Wimpernverlängerung, Wimpernlifting, Permanent Make-Up, Microblading, BB Glow, Hyaluron Pen
Aufgabenstellung
es soll eine preisliste werden, ich möchte die preise selbst einsetzen
produkte:
Wimpernverlängerung:
Natural Look
Auffüllen bis 1-2 Wochen
Auffüllen bis 3-4 Wochen
Ab der 5. Woche Neupreis
Volumen Look
Wimpernlifting inkl. färben
Microblading
Permanent Make-Up:
Powder Brows
Powder Brows Combo (Härchen&Shading)
Wimpernkranzverdichtung
Lidstrich dekorativ
Aquarelle Lips
Lippen Vollschattierung
BB Glow
Hyaluron Pen
Termine nach Vereinbarung

```html
<!DOCTYPE html>
<html lang="de">
<head>
<meta charset="utf-8">
<title>Preisliste – Lidglanz</title>
<link href="https://fonts.googleapis.com/css2?family=Crimson+Pro:wght@400;500&display=swap" rel="stylesheet">
<style>
  :root {
    --pink: #f2a1c6;
    --pink-text: #eda0c3;
    --plum: #5f1d5a;
    --white: #ffffff;
  }
  html, body {
    margin: 0;
    padding: 0;
    width: 1200px;
    height: 2400px;
    overflow: hidden;
    background: var(--white);
  }
  .flyer {
    position: relative;
    width: 1200px;
    height: 2400px;
    font-family: "Crimson Pro", Georgia, serif;
    color: var(--plum);
    overflow: hidden;
  }
  .header-shape {
    position: absolute;
    left: 0;
    top: 0;
    width: 1200px;
    height: 420px;
  }
  .title {
    position: absolute;
    left: 98px;
    top: 60px;
    margin: 0;
    font-weight: 400;
    font-size: 108px;
    letter-spacing: 1px;
    color: var(--plum);
    transform: rotate(-10deg);
    transform-origin: left bottom;
  }
  .section-title {
    position: absolute;
    top: 310px;
    left: 0;
    width: 100%;
    margin: 0;
    text-align: center;
    font-weight: 500;
    font-size: 68px;
    color: var(--plum);
  }
  .price-list {
    position: absolute;
    top: 440px;
    left: 104px;
    width: 944px;
    margin: 0;
    padding: 0;
    list-style: none;
    font-size: 33px;
  }
  .price-row {
    position: relative;
    height: 70.5px;
    line-height: 70.5px;
    white-space: nowrap;
  }
  .price-row.is-sub { color: var(--pink-text); }
  .price-row.is-group { color: var(--plum); }
  .price-fill {
    position: absolute;
    left: 467px;
    width: 391px;
    top: 47px;
    border-bottom: 2px solid currentColor;
  }
  .price-row.is-sub .price-fill { border-bottom-width: 1.5px; }
  .price-fill.is-short { left: 689px; width: 169px; }
  .currency {
    position: absolute;
    left: 864px;
    top: 0;
  }
  .brand {
    position: absolute;
    top: 2000px;
    left: 0;
    width: 100%;
    text-align: center;
    margin: 0;
    font-weight: 400;
    font-size: 92px;
    letter-spacing: 2px;
    color: var(--plum);
  }
  .contact {
    position: absolute;
    top: 2138px;
    font-size: 32px;
    line-height: 48.5px;
    color: var(--plum);
    margin: 0;
    font-style: normal;
  }
  .contact-owner { left: 104px; }
  .contact-owner strong { font-weight: 500; }
  .contact-online { left: 658px; }
  .footer-band {
    position: absolute;
    left: 0;
    bottom: 0;
    width: 100%;
    height: 88px;
    background: var(--plum);
    color: var(--white);
    text-align: center;
    line-height: 88px;
    font-size: 42px;
    letter-spacing: 2px;
  }
</style>
</head>
<body>
<div class="flyer">
  <svg class="header-shape" viewBox="0 0 1200 420" aria-hidden="true">
    <path d="M0 0 H1200 V250 C1000 250 760 240 560 262 C340 286 150 330 0 392 Z" fill="var(--pink)"/>
    <path d="M0 392 C150 330 340 286 560 262 C760 240 1000 250 1200 250 V300 C1060 282 880 268 660 286 C420 306 200 350 0 392 Z" fill="var(--plum)"/>
  </svg>

  <h1 class="title">Preisliste</h1>
  <h2 class="section-title">Produkte:</h2>

  <ul class="price-list">
    <li class="price-row is-group" style="color:var(--plum)">Wimpernverlängerung:</li>
    <li class="price-row is-sub">Natural Look<span class="price-fill"></span><span class="currency">Euro</span></li>
    <li class="price-row is-sub">Auffüllen bis 1-2 Wochen<span class="price-fill"></span><span class="currency">Euro</span></li>
    <li class="price-row is-sub">Auffüllen bis 3-4 Wochen<span class="price-fill"></span><span class="currency">Euro</span></li>
    <li class="price-row is-sub">Ab der 5. Woche Neupreis<span class="price-fill"></span><span class="currency">Euro</span></li>
    <li class="price-row is-group">Volumen Look<span class="price-fill"></span><span class="currency">Euro</span></li>
    <li class="price-row is-sub">Auffüllen bis 1-2 Wochen<span class="price-fill"></span><span class="currency">Euro</span></li>
    <li class="price-row is-sub">Auffüllen bis 3-4 Wochen<span class="price-fill"></span><span class="currency">Euro</span></li>
    <li class="price-row is-sub">Ab der 5. Woche Neupreis<span class="price-fill"></span><span class="currency">Euro</span></li>
    <li class="price-row is-group">Wimpernlifting inkl. färben<span class="price-fill"></span><span class="currency">Euro</span></li>
    <li class="price-row is-group">Microblading<span class="price-fill"></span><span class="currency">Euro</span></li>
    <li class="price-row is-group">Permanent Make-Up:<span class="price-fill"></span><span class="currency">Euro</span></li>
    <li class="price-row is-sub">Powder Brows<span class="price-fill"></span><span class="currency">Euro</span></li>
    <li class="price-row is-sub">Powder Brows Combo (Härchen&amp;Shading)<span class="price-fill is-short"></span><span class="currency">Euro</span></li>
    <li class="price-row is-sub">Wimpernkranzverdichtung<span class="price-fill"></span><span class="currency">Euro</span></li>
    <li class="price-row is-sub">Lidstrich dekorativ<span class="price-fill"></span><span class="currency">Euro</span></li>
    <li class="price-row is-sub">Aquarelle Lips<span class="price-fill"></span><span class="currency">Euro</span></li>
    <li class="price-row is-sub">Lippen Vollschattierung<span class="price-fill"></span><span class="currency">Euro</span></li>
    <li class="price-row is-group">BB Glow<span class="price-fill"></span><span class="currency">Euro</span></li>
    <li class="price-row is-group">Hyaluron Pen<span class="price-fill"></span><span class="currency">Euro</span></li>
  </ul>

  <p class="brand">LIDGLANZ</p>

  <address class="contact contact-owner">
    <strong>Mirabel Tosch</strong><br>
    87999 Talbach/Wiesen<br>
    Tel.: 0176 55501234
  </address>
  <address class="contact contact-online">
    www.lidglanz.de<br>
    facebookseite: lidglanz_studio<br>
    instagram: lidglanz_de
  </address>

  <div class="footer-band">TERMINE NACH VEREINBARUNG</div>
</div>
</body>
</html>
```